Holt & Partners Property Management

I want 4 different cards so that i can mail to my farm once per quarter. I want to go back to a 5X8 card or smaller. I am attaching an example of what we did in the past. I would like the new cards start with the following:
1. Tired of dealing with tenant problems at 6:00 on a Friday Night?
2. Would you like to take you next vacation worry free?
3. Are your tenants paying below market rents?
4. Do your tenant leases fully protect you?
I would like to have one of these "hooks" to lead off each card with a brief explanation of the services we provide. Back of the card can be similar to the one I attached.

Target Market(s)

Income Property Owners that might be in need of a property management company.

Font styles to use
Serif

Requirements
Must have
• 4 separate cards that i can email out each quarter.
• Each card must have a "hook" or "call to action"
Nice to have
• Less verbiage and some catchy graphics or photo
• If you have an idea for catchier calls to action, feel free to submit.
Should not have
• Too many words. The postcard I uploaded has way too much verbiage.

```html
<!DOCTYPE html>
<html lang="en">
<head>
<meta charset="utf-8">
<title>Holt &amp; Partners Property Management – Postcard</title>
<link rel="stylesheet" href="https://fonts.googleapis.com/css2?family=Montserrat:wght@300;400;500;600;700&family=Roboto+Condensed:ital,wght@0,400;0,700;1,400&family=Roboto:wght@400;500&display=swap">
<style>
  :root {
    --stage: #e2e2e2;
    --card-dark: #3b3b3d;
    --ink: #2d2d2d;
    --white: #ffffff;
    --tan: #a69b8a;
    --tan-light: #c9bfae;
    --yellow: #fff200;
    --photo-warm: #6b5644;
    --photo-deep: #2a221d;
  }
  * { box-sizing: border-box; margin: 0; padding: 0; }
  html, body { width: 1006px; height: 1200px; overflow: hidden; }
  body {
    background: radial-gradient(ellipse at center, #f1f1f1 0%, var(--stage) 70%, #d4d4d4 100%);
    position: relative;
    font-family: "Roboto Condensed", Arial, sans-serif;
  }
  .side-label {
    position: absolute;
    left: 52px;
    font-family: "Roboto", Arial, sans-serif;
    font-size: 28px;
    color: #111;
    transform: rotate(-90deg);
    transform-origin: left top;
  }
  .side-label--front { top: 580px; }
  .side-label--back { top: 1132px; }

  .card {
    position: absolute;
    left: 98px;
    width: 810px;
    height: 506px;
    overflow: hidden;
    box-shadow: 0 14px 18px -10px rgba(0,0,0,.35);
  }
  .card--front { top: 70px; background: var(--card-dark); }
  .card--back { top: 623px; background: var(--white); }
  .card svg.card-art { position: absolute; inset: 0; }
  .abs { position: absolute; }

  /* Front */
  .brand { left: 27px; top: 18px; color: var(--white); font-family: "Montserrat", Arial, sans-serif; }
  .brand__name { font-size: 31px; font-weight: 400; letter-spacing: .3px; line-height: 28px; }
  .brand__tag { font-size: 11.5px; font-weight: 600; letter-spacing: 1.1px; margin-top: 20px; }
  .hook { left: 27px; top: 146px; color: var(--white); font-family: "Montserrat", Arial, sans-serif; }
  .hook__lead { font-size: 26px; font-weight: 500; line-height: 34px; }
  .hook__punch { font-size: 50px; font-weight: 700; color: var(--yellow); line-height: 56px; margin-top: 2px; }
  .phone-band {
    left: 0; top: 330px; width: 480px; height: 78px;
    background: linear-gradient(90deg, var(--tan) 0%, #8e8475 55%, rgba(110,103,92,0) 100%);
  }
  .phone-band__icon { position: absolute; left: 26px; top: 17px; width: 42px; height: 46px; background: #e3ddd2; }
  .phone-band__num { position: absolute; left: 80px; top: 2px; font-size: 60px; font-weight: 700; color: var(--white); letter-spacing: .5px; }
  .cta-band { left: 0; top: 408px; width: 560px; height: 58px; padding-left: 26px; background: #262627; font-size: 40px; line-height: 58px; color: var(--yellow); }
  .cta-band strong { color: var(--white); font-weight: 700; }
  .contact-strip { left: 26px; top: 466px; height: 40px; display: flex; align-items: center; gap: 26px; color: var(--white); font-size: 19px; }
  .contact-strip span { display: flex; align-items: center; gap: 8px; }
  .agent-name { left: 532px; top: 338px; width: 100px; text-align: center; font-size: 30px; font-weight: 700; line-height: 32px; color: var(--ink); }

  /* Back */
  .license { left: 0; top: 26px; width: 175px; height: 32px; background: var(--tan); color: var(--white); font-size: 14px; font-weight: 700; line-height: 32px; padding-left: 23px; }
  .quote { left: 34px; top: 76px; width: 302px; font-style: italic; font-size: 12px; line-height: 18.4px; color: var(--white); text-align: justify; }
  .quote::before { content: "\201C"; position: absolute; left: -14px; top: -4px; font-size: 20px; }
  .quote-from { left: 35px; top: 258px; font-size: 19px; color: var(--tan-light); }
  .quote-from strong { font-weight: 700; }
  .address { left: 22px; top: 313px; display: flex; gap: 10px; color: var(--white); font-size: 17px; font-weight: 700; line-height: 22px; }
  .back-cta { left: 0; top: 370px; width: 362px; height: 57px; padding-left: 30px; font-size: 31px; font-weight: 700; line-height: 57px; color: #9a8f7e; white-space: nowrap; }
  .back-contacts { left: 22px; top: 441px; color: var(--white); font-family: "Roboto", Arial, sans-serif; font-size: 15px; font-weight: 500; letter-spacing: .4px; line-height: 30px; }
  .back-contacts span { display: flex; align-items: center; gap: 9px; }
  .stamp-box { left: 676px; top: 69px; width: 88px; height: 88px; border: 1px solid #333; }
  .address-line { left: 497px; width: 267px; height: 1px; background: #999; }
  .back-brand { left: 401px; top: 374px; color: #333; font-family: "Montserrat", Arial, sans-serif; }
  .back-brand__name { font-size: 18px; font-weight: 400; line-height: 17px; }
  .back-brand__tag { font-size: 7.5px; font-weight: 600; letter-spacing: .8px; margin-top: 12px; }
  .back-agent { left: 562px; top: 337px; font-size: 33px; font-weight: 700; color: var(--ink); }
  .back-phone { left: 574px; top: 382px; font-size: 31px; font-weight: 700; color: var(--white); display: flex; align-items: center; gap: 4px; }
</style>
</head>
<body>

<div class="side-label side-label--front">Front</div>
<div class="side-label side-label--back">Back</div>

<!-- FRONT -->
<section class="card card--front">
  <svg class="card-art" width="810" height="506" viewBox="0 0 810 506">
    <defs>
      <linearGradient id="portraitTone" x1="0" y1="0" x2="1" y2="1">
        <stop offset="0" stop-color="var(--photo-warm)"/>
        <stop offset=".6" stop-color="#4a3b31"/>
        <stop offset="1" stop-color="var(--photo-deep)"/>
      </linearGradient>
    </defs>
    <polygon points="170,0 300,0 420,125 370,160" fill="#48484a"/>
    <polygon points="520,0 760,0 810,40 810,300 700,380" fill="#4f4f51"/>
    <polygon points="365,0 465,0 527,62 466,101" fill="var(--white)"/>
    <polygon points="740,0 766,0 810,42 810,68" fill="#1c1c1d"/>
    <polygon points="766,0 810,0 810,42" fill="var(--white)"/>
    <polygon points="740,340 810,280 810,420 790,410" fill="#5c5c5e"/>
    <polygon points="640,440 705,375 810,470 810,506 700,506" fill="var(--white)"/>
    <polygon points="760,470 810,420 810,470 790,470" fill="#1c1c1d"/>
    <polygon points="582,30 786,234 582,436 380,234" fill="var(--white)"/>
    <polygon points="582,37 779,234 582,429 387,234" fill="#2b2b2c"/>
    <g role="img" aria-label="Portrait photo of the two property managers, smiling">
      <polygon points="582,43 773,234 677,334 487,334 393,234" fill="url(#portraitTone)"/>
    </g>
    <polygon points="487,334 677,334 582,429" fill="var(--white)"/>
  </svg>

  <div class="abs brand">
    <div class="brand__name">HOLT &amp;<br>PARTNERS</div>
    <div class="brand__tag">PROPERTY MANAGEMENT</div>
  </div>

  <div class="abs hook">
    <p class="hook__lead">Tired of dealing with<br>Tenant Problems<br>at 6:00 on a</p>
    <p class="hook__punch">Friday Night?</p>
  </div>

  <div class="abs phone-band">
    <span class="phone-band__icon">
      <svg width="42" height="46" viewBox="0 0 42 46"><path d="M15 11c2 0 3 5 3 7s-3 2-3 3c0 3 3 8 6 10 1 0 2-3 4-2s5 3 5 5-3 4-5 4c-8 0-15-13-15-21 0-3 3-6 5-6z" fill="none" stroke="#8a8070" stroke-width="2"/></svg>
    </span>
    <span class="phone-band__num">310-555-0187</span>
  </div>

  <div class="abs cta-band">CALL FOR A <strong>FREE QUOTE</strong></div>

  <div class="abs contact-strip">
    <span>
      <svg width="22" height="22" viewBox="0 0 22 22" fill="none" stroke="#e3ddd2" stroke-width="1.5"><circle cx="11" cy="11" r="9.5"/><ellipse cx="11" cy="11" rx="4.5" ry="9.5"/><path d="M1.5 11h19M3 6h16M3 16h16"/></svg>
      harborbluffestatesproperty.com
    </span>
    <span>
      <svg width="26" height="20" viewBox="0 0 26 20"><rect x="1" y="2" width="24" height="16" fill="#e3ddd2"/><path d="M1 2l12 9 12-9" fill="none" stroke="#3b3b3d" stroke-width="1.6"/></svg>
      glen@glenholtpm.com
    </span>
  </div>

  <div class="abs agent-name">GLEN<br>HOLT</div>
</section>

<!-- BACK -->
<section class="card card--back">
  <svg class="card-art" width="810" height="506" viewBox="0 0 810 506">
    <polygon points="0,0 476,0 316,506 0,506" fill="var(--card-dark)"/>
    <polygon points="450,0 476,0 316,506 290,506" fill="var(--tan)"/>
    <polygon points="0,370 372,370 354,427 0,427" fill="var(--white)"/>
    <polygon points="568,377 810,377 810,427 551,427" fill="var(--tan)"/>
  </svg>

  <div class="abs license">Broker BRE 01987654</div>

  <p class="abs quote">We have had Holt &amp; Partners manage our property since 2009. Since that time we have been very pleased with their services. Phone calls or situations are addressed on a timely basis. It really gives us peace of mind knowing that Glen Holt and his company are taking good care of our property. Also, we recently sold and closed escrow on another property in the South Bay. Glen handled everything to perfection. We would highly recommend Glen Holt and his company to others for any real estate needs. We will be using Glen in the future. He makes it all so easy.&#8221;</p>

  <div class="abs quote-from">FROM <strong>Eleanor R.</strong></div>

  <div class="abs address">
    <svg width="26" height="32" viewBox="0 0 26 32" fill="none" stroke="#fff" stroke-width="2"><path d="M13 23c-5-7-8-10-8-14a8 8 0 0 1 16 0c0 4-3 7-8 14z"/><circle cx="13" cy="9" r="3"/><ellipse cx="13" cy="26" rx="11" ry="3.5"/></svg>
    <div>48 Crescent Bay Plaza, Suite 2<br>Harbor Bluff Estates, CA 90277</div>
  </div>

  <div class="abs back-cta">CALL FOR A FREE QUOTE</div>

  <div class="abs back-contacts">
    <span>
      <svg width="18" height="18" viewBox="0 0 22 22" fill="none" stroke="#e3ddd2" stroke-width="1.6"><circle cx="11" cy="11" r="9.5"/><ellipse cx="11" cy="11" rx="4.5" ry="9.5"/><path d="M1.5 11h19M3 6h16M3 16h16"/></svg>
      harborbluffestatesproperty.com
    </span>
    <span>
      <svg width="20" height="15" viewBox="0 0 26 20"><rect x="1" y="2" width="24" height="16" fill="#e3ddd2"/><path d="M1 2l12 9 12-9" fill="none" stroke="#3b3b3d" stroke-width="1.6"/></svg>
      glen@glenholtpm.com
    </span>
  </div>

  <div class="abs stamp-box"></div>
  <div class="abs address-line" style="top:203px"></div>
  <div class="abs address-line" style="top:239px"></div>
  <div class="abs address-line" style="top:274px"></div>

  <div class="abs back-brand">
    <div class="back-brand__name">HOLT &amp;<br>PARTNERS</div>
    <div class="back-brand__tag">PROPERTY MANAGEMENT</div>
  </div>

  <div class="abs back-agent">GLEN HOLT</div>
  <div class="abs back-phone">
    <svg width="20" height="26" viewBox="0 0 20 26"><path d="M6 3c2 0 3 4 3 6s-2 2-2 3c0 2 2 6 4 7 1 0 2-2 3-1s3 2 3 4-2 3-3 3C8 25 3 15 3 9 3 6 4 3 6 3z" fill="none" stroke="#fff" stroke-width="2"/></svg>
    310-555-0187
  </div>
</section>

</body>
</html>
```